Copper Lark- Hand made fashion accessories

Copper lark is a new business that will be selling hand made fashion accessories for women such as bags, baskets, knecklaces etc. The items are all hand made from Africa. I would like natural colors leaning more to the cardboard rustic look. I would like the card to look simple but elegant at the same time.

Industry/Entity Type

Business

Contact Information for Business Card

www.copperlark-example.com.au
sales@copperlark-example.com.au
Tel: 0427586302

Font styles to use
Decorative
Script

Requirements
Must have
• Earthy and rustic colours. Straw, cardboard etc. Fine black cursive print. One side of card only name
• second side website, email and tel.
Should not have
• No need to have any description of what business sells or does. No pictures of anything.

```html
<!DOCTYPE html>
<html lang="en">
<head>
<meta charset="utf-8">
<title>Copper Lark – Business Card</title>
<link rel="stylesheet" href="https://fonts.googleapis.com/css2?family=Open+Sans:wght@300;400&display=swap">
<style>
  :root {
    --backdrop: #e8e3db;
    --kraft: #b28c68;
    --kraft-edge: #9c7856;
    --ink: #1b1511;
  }
  * { margin: 0; padding: 0; box-sizing: border-box; }
  html, body {
    width: 1200px;
    height: 1023px;
    overflow: hidden;
    background: var(--backdrop);
  }
  .canvas {
    position: relative;
    width: 1200px;
    height: 1023px;
    font-family: "Open Sans", Arial, sans-serif;
    color: var(--ink);
  }
  .card {
    position: absolute;
    left: 320px;
    width: 560px;
    height: 340px;
    background: var(--kraft);
    border: 1px solid var(--kraft-edge);
    border-radius: 3px;
  }
  .card--front { top: 141px; }
  .card--back { top: 541px; }

  .brand-mark {
    position: absolute;
    left: 172px;
    top: 62px;
    width: 216px;
    height: 216px;
    border: 1.5px solid var(--ink);
    border-radius: 50%;
    display: flex;
    align-items: center;
    justify-content: center;
  }
  .brand-name {
    font-size: 30px;
    font-weight: 300;
    color: var(--ink);
    letter-spacing: 1px;
    white-space: nowrap;
  }

  .contact-list {
    position: absolute;
    right: 28px;
    top: 30px;
    list-style: none;
  }
  .contact-item {
    display: flex;
    justify-content: flex-end;
    align-items: center;
    gap: 14px;
    height: 32px;
    font-size: 17px;
    font-weight: 400;
    letter-spacing: 0.4px;
  }
  .contact-icon {
    width: 15px;
    height: 15px;
    flex: none;
  }
</style>
</head>
<body>
<main class="canvas">
  <section class="card card--front" aria-label="Card front">
    <div class="brand-mark">
      <span class="brand-name">Copper Lark</span>
    </div>
  </section>

  <section class="card card--back" aria-label="Card back">
    <ul class="contact-list">
      <li class="contact-item">
        <span>www.copperlark-example.com.au</span>
        <svg class="contact-icon" viewBox="0 0 16 16" aria-hidden="true">
          <rect x="0.5" y="0.5" width="15" height="15" rx="2" fill="var(--ink)"/>
          <circle cx="8" cy="8" r="4.5" fill="none" stroke="var(--kraft)" stroke-width="1.2"/>
          <line x1="3.5" y1="8" x2="12.5" y2="8" stroke="var(--kraft)" stroke-width="1"/>
          <ellipse cx="8" cy="8" rx="2" ry="4.5" fill="none" stroke="var(--kraft)" stroke-width="1"/>
        </svg>
      </li>
      <li class="contact-item">
        <span>sales@copperlark-example.com.au</span>
        <svg class="contact-icon" viewBox="0 0 16 16" aria-hidden="true">
          <rect x="0.5" y="0.5" width="15" height="15" rx="2" fill="var(--ink)"/>
          <rect x="3" y="4.5" width="10" height="7" fill="none" stroke="var(--kraft)" stroke-width="1.2"/>
          <polyline points="3,4.5 8,8.5 13,4.5" fill="none" stroke="var(--kraft)" stroke-width="1.2"/>
        </svg>
      </li>
      <li class="contact-item">
        <span>0427 586 302</span>
        <svg class="contact-icon" viewBox="0 0 16 16" aria-hidden="true">
          <rect x="0.5" y="0.5" width="15" height="15" rx="2" fill="var(--ink)"/>
          <path d="M5 3.5 L6.8 3.5 L7.4 6 L6.2 7 Q7.3 9.2 9 9.8 L10 8.6 L12.5 9.2 L12.5 11 Q12 12.5 10.5 12.5 Q4 11.5 3.5 5 Q3.5 3.8 5 3.5 Z" fill="var(--kraft)"/>
        </svg>
      </li>
    </ul>
  </section>
</main>
</body>
</html>
```